New more attractive design for an old tired look that is high tech but inviting

Need a more modern eye catching design. We are and I/T and MSP and we need a new look. Need a call to action on each page. Needs to be in WordPress. Existing site is quorbelna.com. Needs to work on phones and tablets. The default home page should present us as an MSP/MSSP and direct the viewer to our services we offer.
Updates

Current deadline assigned at project inception has passed before project started

Need extra days to review

Target Market(s)

Our target market is other businesses. We do not target residential customers.

Industry/Entity Type

Business to Business oriented

Coding

Coded - Design and coding required

Number of Pages Required

5+ page

Font styles to use
Sans Serif

Requirements
Must have
• Must have a current relevant design with a call to action on each page.
Nice to have
• Dark background high tech look with people to make it attractive

```html
<!DOCTYPE html>
<html lang="en">
<head>
<meta charset="utf-8">
<title>Quorbelna Solutions – Managed IT &amp; Security</title>
<link rel="stylesheet" href="https://fonts.googleapis.com/css2?family=Poppins:wght@400;500;600;700;800&display=swap">
<style>
:root{
  --red:#c8202f;
  --red-dark:#a91926;
  --navy:#2f3d47;
  --navy-deep:#24313a;
  --ink:#1d2328;
  --muted:#5d656c;
  --light:#f1f2f3;
  --field:#eeeff0;
  --white:#ffffff;
}
*{box-sizing:border-box;margin:0;padding:0}
html,body{width:1200px;height:3900px;overflow:hidden}
body{font-family:"Poppins",sans-serif;color:var(--ink);background:var(--white);position:relative}
.accent{color:var(--red)}
.btn{display:inline-block;font-size:11px;font-weight:600;letter-spacing:.5px;text-transform:uppercase;padding:12px 22px;border:0;text-decoration:none}
.btn-red{background:var(--red);color:var(--white)}
.btn-dark{background:var(--navy);color:var(--white)}
.btn-outline{border:1px solid var(--white);color:var(--white)}

/* header */
.site-header{position:absolute;top:0;left:0;width:1200px;height:92px;display:flex;align-items:center;justify-content:space-between;padding:0 60px}
.brand{display:flex;align-items:center;gap:10px;font-size:26px;font-weight:700;color:var(--navy);text-decoration:none}
.brand-mark{width:14px;height:14px;background:var(--red)}
.main-nav{display:flex;align-items:center;gap:26px;font-size:11px;font-weight:500;text-transform:uppercase}
.main-nav a{color:var(--ink);text-decoration:none}
.nav-phone{display:flex;align-items:center;gap:10px;font-weight:600;font-size:13px}
.phone-dot{width:34px;height:34px;border-radius:50%;background:var(--red);display:flex;align-items:center;justify-content:center}

/* hero */
.hero{position:absolute;top:92px;left:0;width:1200px;height:628px}
.hero-copy{position:absolute;left:60px;top:110px;width:520px}
.hero-copy h1{font-size:62px;line-height:1.08;font-weight:800;color:var(--navy)}
.hero-copy p{margin:22px 0 30px;font-size:15px;line-height:1.6;color:var(--ink);width:380px}
.hero-dots{position:absolute;left:60px;bottom:40px;display:flex;gap:8px}
.hero-dots span{width:46px;height:3px;background:#c9ccd0}
.hero-dots span.on{background:var(--navy)}
.hero-photo{position:absolute;right:0;top:0;width:590px;height:628px;background:linear-gradient(135deg,#0d2a45 0%,#1d4f78 45%,#0f2235 100%)}

/* about */
.about{position:absolute;top:720px;left:0;width:1200px;height:400px;background:var(--light);text-align:center;padding-top:100px}
.about h2{font-size:36px;font-weight:700;color:var(--navy)}
.about p{width:700px;margin:18px auto 28px;font-size:13px;line-height:1.75;color:var(--muted)}

/* expertise */
.expertise{position:absolute;top:1120px;left:0;width:1200px;height:660px}
.expertise-panel{position:absolute;left:120px;top:20px;width:620px;height:620px;background:var(--navy);clip-path:polygon(0 0,100% 0,100% 78%,78% 100%,0 100%);padding:120px 0 0 70px;color:var(--white)}
.expertise-panel h2{font-size:36px;line-height:1.25;font-weight:700}
.expertise-panel p{width:300px;margin:22px 0 26px;font-size:12px;line-height:1.7;color:#d5dadd}
.service-grid{position:absolute;left:620px;top:70px;width:430px;height:390px;background:var(--red);display:grid;grid-template-columns:1fr 1fr;gap:14px;padding:26px}
.service-card{background:var(--red-dark);display:flex;flex-direction:column;align-items:center;justify-content:center;text-align:center;color:var(--white);font-size:13px;font-weight:600;line-height:1.35;gap:12px}
.touch-line{position:absolute;left:800px;top:500px;font-size:22px;font-weight:600;line-height:1.35;color:var(--navy)}

/* stats */
.stats{position:absolute;top:1800px;left:60px;width:1080px;height:200px;display:grid;grid-template-columns:repeat(4,1fr)}
.stat{text-align:center;border-right:1px solid #d6d9dc;padding-top:40px}
.stat:last-child{border-right:0}
.stat strong{display:block;font-size:50px;font-weight:600;color:var(--navy)}
.stat strong small{font-size:20px}
.stat span{display:block;margin-top:8px;font-size:11px;line-height:1.5;color:var(--muted)}

/* data center */
.datacenter{position:absolute;top:2130px;left:0;width:1010px;height:500px;background:var(--navy-deep);clip-path:polygon(0 0,100% 0,100% 82%,91% 100%,0 100%);padding:150px 0 0 140px;color:var(--white)}
.datacenter h2{font-size:38px;line-height:1.2;font-weight:700}
.datacenter p{margin:14px 0 26px;font-size:13px;line-height:1.6;color:#d5dadd;width:300px}
.dc-card{position:absolute;top:2185px;left:650px;width:520px;height:540px;background:var(--red);padding:36px}
.dc-grid{display:grid;grid-template-columns:1fr 1fr;gap:10px}
.dc-item{height:170px;background:rgba(255,255,255,.12);color:var(--white);display:flex;flex-direction:column;align-items:center;justify-content:center;text-align:center;gap:8px;padding:0 18px}
.dc-item b{font-size:14px;font-weight:600}
.dc-item span{font-size:10px;line-height:1.5;color:#f5d6d9}
.dc-item.plain{background:transparent}
.dc-card h3{margin-top:40px;font-size:18px;font-weight:600;color:var(--white);line-height:1.4;width:360px}

/* contact */
.contact{position:absolute;top:2800px;left:0;width:1200px;text-align:center}
.contact h2{font-size:36px;font-weight:700;color:var(--navy)}
.contact-form{width:700px;margin:50px auto 0;display:grid;grid-template-columns:1fr 1fr;column-gap:30px;row-gap:22px;text-align:left}
.contact-form label{display:block;font-size:10px;font-weight:600;text-transform:uppercase;margin-bottom:6px}
.contact-form label em{color:var(--red);font-style:normal}
.field{height:52px;background:var(--field);font-size:11px;color:#9aa0a5;display:flex;align-items:center;padding-left:18px}
.submit{height:52px;background:var(--red);color:var(--white);font-size:13px;font-weight:600;display:flex;align-items:center;justify-content:center;gap:90px;align-self:end}

/* footer */
.site-footer{position:absolute;top:3290px;left:0;width:1200px;height:610px;background:var(--navy);color:var(--white)}
.footer-brand{text-align:center;padding-top:50px;font-size:40px;font-weight:700;display:flex;justify-content:center;align-items:center;gap:12px}
.footer-brand .brand-mark{width:18px;height:18px}
.social{display:flex;justify-content:flex-end;gap:10px;padding:34px 270px 0 0}
.social span{width:30px;height:30px;border-radius:50%;border:1px solid rgba(255,255,255,.6)}
.footer-cols{display:grid;grid-template-columns:repeat(4,1fr);width:900px;margin:30px auto 0;padding-top:40px;border-top:1px solid rgba(255,255,255,.2)}
.footer-cols h4{font-size:15px;font-weight:600;margin-bottom:16px}
.footer-cols li{list-style:none;font-size:11px;line-height:2;color:#cfd5d9}
.contact-row{display:flex;gap:10px;margin-bottom:12px}
.contact-row i{width:10px;height:10px;border-radius:50%;background:var(--red);margin-top:6px;flex:none}
.copyright{position:absolute;bottom:40px;width:100%;text-align:center;font-size:11px;color:#cfd5d9}
</style>
</head>
<body>

<header class="site-header">
  <a class="brand" href="#"><span class="brand-mark"></span>Quorbelna</a>
  <nav class="main-nav">
    <svg width="14" height="14" viewBox="0 0 14 14"><path d="M1 7 7 1l6 6v6H9V9H5v4H1z" fill="#c8202f"/></svg>
    <a href="#">Services</a><a href="#">About</a><a href="#">Contact</a>
    <a class="btn btn-dark" href="#">Schedule a Call</a>
    <span class="nav-phone"><span class="phone-dot"><svg width="14" height="14" viewBox="0 0 24 24"><path d="M6.6 10.8a15 15 0 0 0 6.6 6.6l2.2-2.2c.3-.3.7-.4 1-.2 1.1.4 2.3.6 3.6.6.6 0 1 .4 1 1V20c0 .6-.4 1-1 1A17 17 0 0 1 3 4c0-.6.4-1 1-1h3.5c.6 0 1 .4 1 1 0 1.3.2 2.5.6 3.6.1.3 0 .7-.2 1z" fill="#fff"/></svg></span>555-014-2290</span>
  </nav>
</header>

<section class="hero">
  <div class="hero-copy">
    <h1>IT Solutions That <span class="accent">Power</span> Your Business</h1>
    <p>Managed Services, Cybersecurity, and 24/7 Support Tailored to Fit Your Business Needs.</p>
    <a class="btn btn-red" href="#">Get a Free Audit</a>
  </div>
  <div class="hero-dots"><span class="on"></span><span></span><span></span></div>
  <div class="hero-photo" role="img" aria-label="Two IT engineers working with a tablet in a blue-lit server room"></div>
</section>

<section class="about">
  <h2>About <span class="accent">Quorbelna</span> Solutions</h2>
  <p>Like most great businesses Quorbelna Solutions began in a garage during the summer of 1995 in Brenmoor, ST. It was a part time venture by Dalen Marsh and his business partner Orrin Vale. They had discovered an opportunity in technology sales and service after a combined 30 years at Halvert Power in information technology. By 2000, the two set out on their own!</p>
  <a class="btn btn-dark" href="#">Show More</a>
</section>

<section class="expertise">
  <div class="expertise-panel">
    <h2>Our IT <span class="accent">Expertise</span>,<br>Your Success.</h2>
    <p>We offer colocation, virtualization, storage as a service and disaster recovery out of our own enterprise grade data center.</p>
    <a class="btn btn-outline" href="#">View All Services</a>
  </div>
  <div class="service-grid">
    <div class="service-card"><svg width="40" height="40" viewBox="0 0 40 40" fill="none" stroke="#fff" stroke-width="2"><circle cx="20" cy="20" r="8"/><path d="M20 4v6M20 30v6M4 20h6M30 20h6M9 9l4 4M27 27l4 4M31 9l-4 4M13 27l-4 4"/></svg>Managed<br>Cybersecurity</div>
    <div class="service-card"><svg width="40" height="40" viewBox="0 0 40 40" fill="none" stroke="#fff" stroke-width="2"><rect x="14" y="4" width="12" height="9"/><rect x="4" y="27" width="12" height="9"/><rect x="24" y="27" width="12" height="9"/><path d="M20 13v7M10 27v-7h20v7"/></svg>Managed Networks for MDUs</div>
    <div class="service-card"><svg width="40" height="40" viewBox="0 0 40 40" fill="none" stroke="#fff" stroke-width="2"><rect x="6" y="6" width="28" height="8"/><rect x="6" y="16" width="28" height="8"/><rect x="6" y="26" width="28" height="8"/><circle cx="11" cy="10" r="1"/><circle cx="11" cy="20" r="1"/><circle cx="11" cy="30" r="1"/></svg>Data Center<br>Services</div>
    <div class="service-card"><svg width="40" height="40" viewBox="0 0 40 40" fill="none" stroke="#fff" stroke-width="2"><path d="M6 34c10 0 6-14 14-14s4-14 14-14"/><circle cx="6" cy="34" r="3"/><circle cx="34" cy="6" r="3"/></svg>Low Voltage<br>Wiring</div>
  </div>
  <p class="touch-line">Interested in Quorbelna<br>Solutions <span class="accent">Get in touch!</span></p>
</section>

<section class="stats">
  <div class="stat"><strong>250<small>+</small></strong><span>Projects in Banking</span></div>
  <div class="stat"><strong>100<small>Mn</small></strong><span>Loan transactions/year through<br>our system</span></div>
  <div class="stat"><strong>14<small>Mn</small></strong><span>New loans booked per minute<br>(during peak time)</span></div>
  <div class="stat"><strong>18</strong><span>New loans booked per minute<br>(during peak time)</span></div>
</section>

<section class="datacenter">
  <h2>Your <span class="accent">Data</span> Center,<br>Your Way</h2>
  <p>From single colocated servers to fully redundant virtualized environments.</p>
  <a class="btn" style="background:#fff;color:var(--navy)" href="#">More About Data Center Services</a>
</section>
<aside class="dc-card">
  <div class="dc-grid">
    <div class="dc-item"><svg width="30" height="30" viewBox="0 0 30 30" fill="none" stroke="#fff" stroke-width="2"><path d="M15 3l3.5 7 7.5 1-5.5 5 1.5 8-7-4-7 4 1.5-8L4 11l7.5-1z"/></svg><b>A True Partner</b><span>Our team works with you to plan every step of the way.</span></div>
    <div class="dc-item"><svg width="30" height="30" viewBox="0 0 30 30" fill="none" stroke="#fff" stroke-width="2"><path d="M15 3l10 4v7c0 7-5 11-10 13C10 25 5 21 5 14V7z"/><path d="M10 15l4 4 6-7"/></svg><b>High Security</b><span>Our data center is a Tier III standard secure facility.</span></div>
    <div class="dc-item"><svg width="30" height="30" viewBox="0 0 30 30" fill="none" stroke="#fff" stroke-width="2"><circle cx="15" cy="16" r="11"/><path d="M15 10v6l4 3M12 3h6"/></svg><b>Availability</b><span>The facility is powered by two separate utility feeds.</span></div>
    <div class="dc-item plain"><svg width="34" height="20" viewBox="0 0 34 20" fill="none" stroke="#fff" stroke-width="2"><path d="M2 10h28M22 2l8 8-8 8"/></svg></div>
  </div>
  <h3>Reimagine Lending with Quorbelna Solution Factory Today!</h3>
</aside>

<section class="contact">
  <h2>Get In <span class="accent">Touch</span> With Us</h2>
  <form class="contact-form">
    <div><label>First Name<em>*</em></label><div class="field">Enter your name</div></div>
    <div><label>Last Name<em>*</em></label><div class="field">Enter your name</div></div>
    <div><label>Address<em>*</em></label><div class="field">Enter your address</div></div>
    <div><label>City State<em>*</em></label><div class="field">Enter city state</div></div>
    <div><label>Email<em>*</em></label><div class="field">Enter your email</div></div>
    <div class="submit">SUBMIT <svg width="14" height="14" viewBox="0 0 24 24"><path d="M2 21 23 12 2 3v7l15 2-15 2z" fill="#fff"/></svg></div>
  </form>
</section>

<footer class="site-footer">
  <div class="footer-brand"><span class="brand-mark" style="background:var(--red)"></span>Quorbelna</div>
  <div class="social"><span></span><span></span><span></span><span></span><span></span></div>
  <div class="footer-cols">
    <div><h4>Quick Links</h4><ul><li>Home</li><li>Services</li><li>About</li><li>Contact</li></ul></div>
    <div><h4>Our Services</h4><ul><li>Cybersecurity</li><li>Managed Networks for MDUs</li><li>Data Center Services</li><li>Low Voltage Wiring</li><li>Office IT Support</li></ul></div>
    <div><h4>Information</h4><ul><li>Privacy Policy</li><li>Terms of Use</li><li>Disclaimer</li><li>Sitemap</li></ul></div>
    <div><h4>Contact Info</h4>
      <div class="contact-row"><i></i><ul><li>Location</li><li>48 Larkfield Rd, Brenmoor, ST 00412</li></ul></div>
      <div class="contact-row"><i></i><ul><li>Phone</li><li>555-014-2290</li></ul></div>
    </div>
  </div>
  <p class="copyright">2025 © Quorbelna Solutions LLC · quorbelna.com</p>
</footer>

</body>
</html>
```